Venture Capital and Sales/Marketing Consultancy Business Needs a Wordpress Design

I need a new web site design to replace our current site built based on Wordpress. Existing hostarvel wordpress hosting can be used. Completely new design, new content and new features can be added. This is a web site for information purposes ONLY. My company offer consulting services to start up or high growth technology companies to help them with financing (venture Capital or angel investment) and marketing/sales/product management expertise. We focus on driving growth through our access to venture capitals and business development strategies. We've helped many start up companies in the past - through my consulting business operating under my name. Now I have turned this business into an organization offering not only sales/marketing expertise but also investment support to help those start up companies.

Target Market(s)

Early Stage Technology Start-ups, Technology Companies with independent intellectual properties. Venture Capital and investment companies looking into technology investment. Companies looking into market expansions in North America and APAC especially China). Product seeking business development partners to reduce marketing and operational risk in developing North American and APAC markets. Technologies demanding Intellectual Property protection in North American and Chinese market.

Industry/Entity Type

Investment

Font styles to use
Sans Serif

Colors
ffcf3e

Requirements
Must have
• Basic features such as Newsfeeds to News page.
• Following pages are required: About Us, Projects, Partners and Contact Us
• Designer will also help with:
• Implementing the design into the current wordpress account hosted by hostarvel.
• All Graphics used in the design need to be included.
Nice to have
• A proposal submission page allow submission of project proposal in PDF format only. Files submitted can be automatically forwarded to an email alias.

```html
<!DOCTYPE html>
<html lang="en">
<head>
<meta charset="utf-8">
<title>Veltaris — Discuss Ideas, Make It Happen</title>
<link rel="stylesheet" href="https://fonts.googleapis.com/css2?family=Open+Sans:wght@400;600;700;800&display=swap">
<style>
:root{
  --gold:#d99a0e;
  --gold-deep:#a97400;
  --gold-light:#ffcf3e;
  --dark:#1c1c1c;
  --ink:#333;
  --muted:#777;
  --rule:#e2e2e2;
  --paper:#ffffff;
  --soft:#f3f3f3;
  --bar:#4d4d4d;
  --alert:#c4302b;
}
*{margin:0;padding:0;box-sizing:border-box}
html,body{width:1200px;height:3051px;overflow:hidden}
body{font-family:"Open Sans",Arial,sans-serif;color:var(--ink);background:var(--paper);position:relative}
.section{position:absolute;left:0;width:1200px}

/* hero */
.hero{top:0;height:485px;background:linear-gradient(180deg,#6b6e78 0%,#c9a27a 38%,#e8c07e 48%,#7a6550 60%,#3a3330 100%)}
.hero-brand{position:absolute;left:18px;top:16px;display:flex;align-items:center;gap:8px;color:var(--gold-light);font-weight:700;font-size:15px}
.hero-brand i{display:block;width:12px;height:12px;background:var(--gold-light)}
.hero-title{position:absolute;top:272px;width:100%;text-align:center;color:#fff;font-size:58px;font-weight:700;letter-spacing:-.5px}
.hero-sub{position:absolute;top:390px;width:100%;text-align:center;color:#fff;font-size:26px;font-weight:400}

/* nav */
.nav{top:485px;height:57px;background:var(--gold)}
.nav-brand{position:absolute;left:160px;top:0;height:57px;width:165px;background:var(--gold-deep);color:#fff;font-weight:800;font-size:20px;display:flex;align-items:center;justify-content:center;letter-spacing:.5px}
.nav-links{position:absolute;left:600px;top:0;height:57px;display:flex;gap:40px;align-items:center;list-style:none}
.nav-links li{color:#fff;font-size:12px;font-weight:700;text-transform:uppercase}

/* welcome */
.welcome{top:542px;height:306px}
.welcome h2{position:absolute;left:160px;top:48px;color:var(--gold);font-size:26px;font-weight:800}
.welcome .body{position:absolute;left:160px;top:98px;width:570px;font-size:12px;line-height:17px;color:var(--muted)}
.welcome .body p+p{margin-top:10px}
.btn{display:inline-block;background:var(--gold);color:#fff;font-size:12px;font-weight:700;padding:6px 16px;margin-top:18px}
.welcome .facts{position:absolute;left:850px;top:50px;width:190px;list-style:none}
.welcome .facts li{color:var(--gold);font-size:12px;font-weight:600;line-height:16px;margin-bottom:16px}

/* video */
.video{top:848px;height:322px;background:linear-gradient(180deg,#262626,#161616)}
.video h2{position:absolute;left:160px;top:100px;color:#fff;font-size:36px;font-weight:400;line-height:44px;letter-spacing:-.5px}
.video h2 span{color:var(--gold-light)}
.video-frame{position:absolute;left:458px;top:30px;width:560px;height:268px;background:linear-gradient(135deg,#6d5c48,#b8a58a 45%,#4d3f33)}
.video-controls{position:absolute;left:0;bottom:0;width:100%;height:26px;background:rgba(20,20,20,.85);display:flex;align-items:center;gap:10px;padding:0 12px}
.video-controls .track{flex:1;height:4px;background:#555}
.video-controls .track b{display:block;width:8%;height:4px;background:var(--gold-light)}

/* about */
.about{top:1170px;height:406px}
.section-title{text-align:center;color:var(--gold);font-size:26px;font-weight:800}
.about .section-title{position:absolute;top:52px;width:100%}
.about .tagline{position:absolute;top:90px;width:100%;text-align:center;font-size:11px;letter-spacing:3px;color:var(--muted)}
.about .tagline::before,.about .tagline::after{content:"";display:inline-block;width:70px;height:1px;background:var(--rule);vertical-align:middle;margin:0 12px}
.services{position:absolute;left:160px;top:160px;width:880px;display:flex;list-style:none}
.service{width:220px;text-align:center;padding:0 14px}
.service svg{display:block;margin:0 auto 22px}
.service h3{font-size:13px;font-weight:800;text-transform:uppercase;color:var(--dark);margin-bottom:10px}
.service.active h3{color:var(--gold)}
.service p{font-size:11px;line-height:16px;color:var(--muted)}
.service .more{display:inline-block;margin-top:18px;font-size:10px;color:var(--muted);text-transform:uppercase;padding-bottom:3px}
.service.active .more{color:var(--gold);border-bottom:2px solid var(--gold)}

/* testimonials */
.testimonials{top:1576px;height:356px;background:var(--gold)}
.testimonials h2{position:absolute;left:160px;top:70px;color:#fff;font-size:22px;font-weight:800}
.avatar{position:absolute;left:540px;top:92px;width:120px;height:120px;border-radius:50%;border:5px solid #fff;background:radial-gradient(circle at 50% 40%,#cfa98a,#7b6a5a)}
.quote{position:absolute;left:200px;top:232px;width:800px;text-align:center;color:#fff;font-size:12px;line-height:18px;font-weight:600}
.cite{position:absolute;top:300px;width:100%;text-align:center;color:#fff;font-size:11px;line-height:15px}
.cite b{display:block;font-weight:700}
.arrow{position:absolute;top:236px}

/* events & news */
.feeds{top:1932px;height:526px;background:var(--soft)}
.feeds h2{color:var(--gold);font-size:22px;font-weight:800;text-transform:uppercase}
.events{position:absolute;left:160px;top:50px;width:430px}
.event{margin-top:14px}
.event-bar{display:flex;height:34px;background:var(--bar);color:#fff;font-size:12px;font-weight:700;align-items:center}
.event-bar .date{width:70px;height:34px;background:var(--gold);display:flex;align-items:center;justify-content:center;font-size:11px}
.event-bar .name{padding-left:14px;text-transform:uppercase}
.event-body{display:flex;gap:22px;margin-top:12px}
.thumb{width:76px;height:76px;background:#cfcfcf;flex:none}
.event-body p{font-size:11px;line-height:16px;color:var(--muted)}
.news{position:absolute;left:636px;top:50px;width:404px;border-left:1px solid var(--rule)}
.news-list{list-style:none;margin-top:14px}
.news-item{display:flex;gap:20px;padding:16px 0 12px;border-bottom:1px solid var(--rule)}
.news-item .thumb{width:70px;height:70px}
.news-item p{font-size:11px;line-height:16px;color:var(--muted)}
.news-item .meta{display:block;text-align:right;font-size:10px;margin-top:4px;color:var(--muted)}
.news-item .meta b{color:var(--alert);font-weight:700}

/* startups */
.startups{top:2458px;height:508px}
.startups h2{position:absolute;left:160px;top:36px;color:var(--gold);font-size:22px;font-weight:800;text-transform:uppercase}
.grid{position:absolute;left:160px;top:84px;width:880px;display:grid;grid-template-columns:repeat(4,220px);grid-auto-rows:187px;list-style:none}
.tile{display:flex;align-items:center;justify-content:center;font-size:18px;font-weight:600;letter-spacing:1px;text-transform:uppercase;color:#fff}
.tile.light{color:var(--ink)}
.t1{background:#1a8a7c}
.t2{background:#efefef}
.t3{background:#157a66}
.t4{background:#fff}
.t5{background:#3a1b21}
.t6{background:#fff}
.t7{background:#2b1a1d}
.t8{background:#111}

/* footer */
.footer{top:2966px;height:85px;border-top:1px solid var(--rule)}
.footer p{text-align:center;font-size:11px;color:var(--muted);margin-top:34px;text-transform:uppercase}
</style>
</head>
<body>

<header class="section hero" role="img" aria-label="Photograph of an open road stretching to the horizon under a golden sunset sky">
  <div class="hero-brand"><i></i>Veltaris</div>
  <h1 class="hero-title">Discuss Ideas, Make It Happen</h1>
  <p class="hero-sub">We Know &amp; Works</p>
</header>

<nav class="section nav">
  <div class="nav-brand">VELTARIS</div>
  <ul class="nav-links">
    <li>Home</li><li>About</li><li>Startups</li><li>Blog</li><li>Research</li><li>Legal</li>
  </ul>
</nav>

<section class="section welcome">
  <h2>HELLO &amp; WELCOME</h2>
  <div class="body">
    <p>We help early stage technology companies find the capital and market reach they need to grow. Our partners bring years of venture, sales and product experience to every founder we meet.</p>
    <p>From first pitch to expansion across North America and Asia Pacific, we work beside founders on financing, go to market planning and business development. We connect promising teams with investors who understand technology and protect the ideas that make them valuable. Our network spans angel groups, venture funds and strategic partners ready to open new markets.</p>
    <span class="btn">Read more</span>
  </div>
  <ul class="facts">
    <li>Since 2005, we've funded over 300 startups</li>
    <li>Our companies have a combined valuation of over $10B</li>
    <li>Connect to a community of over 1,400 founders</li>
    <li>Complete a market &amp; partnership review for leading early stage startups</li>
  </ul>
</section>

<section class="section video">
  <h2>Watch Incuvest's<br>Interview with<br><span>Veltaris</span> Founders</h2>
  <div class="video-frame" role="img" aria-label="Video still of two people in conversation across a table in an office">
    <div class="video-controls">
      <svg width="10" height="12" viewBox="0 0 10 12"><path d="M0 0L10 6L0 12Z" fill="#ccc"/></svg>
      <div class="track"><b></b></div>
      <svg width="14" height="12" viewBox="0 0 14 12"><path d="M0 4H4L8 0V12L4 8H0Z" fill="#ccc"/></svg>
    </div>
  </div>
</section>

<section class="section about">
  <h2 class="section-title">ABOUT NORVANE AGENCY</h2>
  <p class="tagline">GROWTH BUILT ON TRUST AND INSIGHT</p>
  <ul class="services">
    <li class="service">
      <svg width="60" height="60" viewBox="0 0 60 60"><rect x="12" y="12" width="36" height="36" transform="rotate(45 30 30)" fill="none" stroke="#555" stroke-width="2"/><path d="M30 38c-6-5-9-8-9-11a4.5 4.5 0 0 1 9-1a4.5 4.5 0 0 1 9 1c0 3-3 6-9 11z" fill="none" stroke="#555" stroke-width="2"/></svg>
      <h3>Venture Capitals</h3>
      <p>Access to funds and angel groups that back early technology teams with patient capital.</p>
      <span class="more">Learn more</span>
    </li>
    <li class="service">
      <svg width="60" height="60" viewBox="0 0 60 60"><rect x="12" y="12" width="36" height="36" transform="rotate(45 30 30)" fill="none" stroke="#555" stroke-width="2"/><circle cx="30" cy="28" r="6" fill="none" stroke="#555" stroke-width="2"/><path d="M27 34h6v4h-6z" fill="#555"/></svg>
      <h3>Development Strategies</h3>
      <p>Clear plans for sales, marketing and product that turn ideas into steady revenue.</p>
      <span class="more">Learn more</span>
    </li>
    <li class="service active">
      <svg width="60" height="60" viewBox="0 0 60 60"><rect x="12" y="12" width="36" height="36" transform="rotate(45 30 30)" fill="#d99a0e"/><path d="M22 36l6-6 4 4 8-10" fill="none" stroke="#fff" stroke-width="2.5"/></svg>
      <h3>High Growth Technology</h3>
      <p>Support for teams with strong intellectual property ready to scale into new regions.</p>
      <span class="more">Learn more</span>
    </li>
    <li class="service">
      <svg width="60" height="60" viewBox="0 0 60 60"><rect x="12" y="12" width="36" height="36" transform="rotate(45 30 30)" fill="none" stroke="#555" stroke-width="2"/><path d="M22 33h16M30 25v16M24 27h12" fill="none" stroke="#555" stroke-width="2"/></svg>
      <h3>Investment Support</h3>
      <p>Guidance through due diligence, term sheets and partner talks from start to close.</p>
      <span class="more">Learn more</span>
    </li>
  </ul>
</section>

<section class="section testimonials">
  <h2>TESTIMONIALS</h2>
  <div class="avatar" role="img" aria-label="Portrait photo of a smiling client"></div>
  <svg class="arrow" style="left:64px" width="26" height="26" viewBox="0 0 26 26"><rect x="5" y="5" width="16" height="16" transform="rotate(45 13 13)" fill="none" stroke="#fff" stroke-width="2"/></svg>
  <svg class="arrow" style="left:1010px" width="26" height="26" viewBox="0 0 26 26"><rect x="5" y="5" width="16" height="16" transform="rotate(45 13 13)" fill="none" stroke="#fff" stroke-width="2"/></svg>
  <p class="quote">Working with this team changed how we raised our first round. They knew the right investors, prepared us for every meeting and helped us shape a sales plan that opened doors in two new markets within a single year.</p>
  <p class="cite"><b>DANIEL MERCER</b>CEO, FOUNDER</p>
</section>

<section class="section feeds">
  <div class="events">
    <h2>Events</h2>
    <div class="event">
      <div class="event-bar"><span class="date">12 SEP</span><span class="name">Projects Hiring Celebration</span></div>
      <div class="event-body"><div class="thumb" role="img" aria-label="Event photo"></div><p>Founders and investors gather to share progress, meet new partners and welcome the latest teams joining our growing program this season.</p></div>
    </div>
    <div class="event">
      <div class="event-bar"><span class="date">12 SEP</span><span class="name">Projects Hiring Celebration</span></div>
      <div class="event-body"><div class="thumb" role="img" aria-label="Event photo"></div><p>Founders and investors gather to share progress, meet new partners and welcome the latest teams joining our growing program this season.</p></div>
    </div>
    <div class="event">
      <div class="event-bar"><span class="date">12 SEP</span><span class="name">Projects Hiring Celebration</span></div>
      <div class="event-body"><div class="thumb" role="img" aria-label="Event photo"></div><p>Founders and investors gather to share progress, meet new partners and welcome the latest teams joining our growing program this season.</p></div>
    </div>
  </div>
  <div class="news">
    <h2>News</h2>
    <ul class="news-list">
      <li class="news-item"><div class="thumb" role="img" aria-label="News photo"></div><p>Our portfolio company closes a new seed round and plans to grow its team across two regions.<span class="meta">21 AUG 2014 | <b>MORE</b></span></p></li>
      <li class="news-item"><div class="thumb" role="img" aria-label="News photo"></div><p>Our portfolio company closes a new seed round and plans to grow its team across two regions.<span class="meta">21 AUG 2014 | <b>MORE</b></span></p></li>
      <li class="news-item"><div class="thumb" role="img" aria-label="News photo"></div><p>Our portfolio company closes a new seed round and plans to grow its team across two regions.<span class="meta">21 AUG 2014 | <b>MORE</b></span></p></li>
      <li class="news-item"><div class="thumb" role="img" aria-label="News photo"></div><p>Our portfolio company closes a new seed round and plans to grow its team across two regions.<span class="meta">21 AUG 2014 | <b>MORE</b></span></p></li>
    </ul>
  </div>
</section>

<section class="section startups">
  <h2>Startups</h2>
  <ul class="grid">
    <li class="tile t1">Amarelle</li>
    <li class="tile t2 light">Corvetta</li>
    <li class="tile t3">Lumen Roast</li>
    <li class="tile t4 light">Plume Drift</li>
    <li class="tile t5">Tonecraft</li>
    <li class="tile t6 light">Growth Sages</li>
    <li class="tile t7">Lotusa</li>
    <li class="tile t8">Orbis</li>
  </ul>
</section>

<footer class="section footer">
  <p>© 2014 Norvane Agency. All rights reserved.</p>
</footer>

</body>
</html>
```